Flyer for an IT consultancy firm

We are an IT consultancy firm based in Iceland. We have a website at: www.brimvolt.com where you can get acquainted with our activities.
We require a double-sided flyer in A4 format to be handed out in conferences, trade shows etc. The flyer is basically a summarized overview of our range of services.

The deliverable should incorporate some visual elements that are relevant to our line of business such as:
• computers
• cybersecurity
• networks
Also, it would be nice to have visuals relating to Icelandic geography, to further emphasize our local roots. Some suggested keywords:
• volcano
• aurora borealis
• waterfall
• glacier

NB: the flyer will be printed out, therefore image resolution needs to be high enough to render nicely on paper.
The primary colors would be red, black and white – in line with our logo. But there is freedom to diverge and go for a different color scheme.

The logo should be present on the top front of the flyer. The URL www.brimvolt.com needs to be mentioned prominently, for example at the bottom of the page.

Examples of design we like:
• https://www.pixelbazaar.net/design/24252027
• https://www.pixelbazaar.net/design/24291120

Attached:
• the text for the brochure in PDF format
• our logo in vector format

IT, software, cybersecurity

EB3D1F
EC4F4E
F09395
F8D3D4
FCEDEE

• existing logo, and visuals related to computer, networks etc
• Icelandic geography/landscapes

```html
<!DOCTYPE html>
<html lang="en">
<head>
<meta charset="UTF-8">
<title>Brimvolt – IT Consultancy Flyer</title>
<link href="https://fonts.googleapis.com/css2?family=Montserrat:ital,wght@0,400;0,600;0,700;0,800;1,400;1,600&display=swap" rel="stylesheet">
<style>
  :root {
    --backdrop: #c4c4c4;
    --paper: #f6f6f6;
    --ink: #3a3a3a;
    --ink-strong: #1e1e1e;
    --brand-red: #9a0b0b;
    --band-red: #8c0606;
    --header-dark: #16181d;
    --header-sky: #3a3f4c;
    --white: #ffffff;
    --faint: #e2e2e2;
  }
  * { box-sizing: border-box; margin: 0; padding: 0; }
  html, body { width: 1200px; height: 800px; overflow: hidden; }
  body {
    background: var(--backdrop);
    font-family: "Montserrat", sans-serif;
    color: var(--ink);
    display: flex;
    justify-content: center;
    align-items: center;
    gap: 40px;
  }
  .page {
    position: relative;
    width: 520px;
    height: 736px;
    background: linear-gradient(180deg, var(--white) 0%, var(--paper) 100%);
    box-shadow: 0 10px 30px rgba(0,0,0,0.18);
    overflow: hidden;
    display: flex;
    flex-direction: column;
  }
  .page-band {
    position: absolute;
    left: 0; right: 0; bottom: 0;
    height: 26px;
    background: var(--band-red);
  }

  /* Front */
  .hero {
    position: relative;
    height: 172px;
    padding: 26px 32px 0;
    color: var(--white);
  }
  .hero-photo {
    position: absolute; inset: 0;
    background: linear-gradient(180deg, var(--header-sky) 0%, #232730 55%, var(--header-dark) 100%);
  }
  .hero-content { position: relative; }
  .brand {
    display: flex; align-items: center; gap: 10px;
    margin-bottom: 10px;
  }
  .brand-dot {
    width: 26px; height: 26px;
    border: 2px solid var(--white);
    border-radius: 50%;
  }
  .brand-name {
    font-weight: 700;
    font-size: 17px;
    letter-spacing: 1px;
    color: var(--white);
  }
  .hero-title {
    font-weight: 700;
    font-size: 19px;
    line-height: 1.22;
    margin-bottom: 8px;
  }
  .hero-sub {
    font-size: 11.5px;
    line-height: 1.35;
    max-width: 260px;
  }

  .front-body { padding: 20px 36px 0; }
  .section { margin-bottom: 16px; }
  .section-title {
    color: var(--brand-red);
    font-weight: 800;
    font-size: 12.5px;
    line-height: 1.2;
    text-transform: uppercase;
    margin-bottom: 4px;
  }
  .section-text {
    font-size: 9.6px;
    line-height: 1.45;
  }
  .section-text.italic { font-style: italic; }
  .section-cta {
    font-size: 9.6px;
    font-weight: 600;
    color: var(--ink-strong);
    margin-top: 3px;
  }
  .section-cta.italic { font-style: italic; }

  .photo-row {
    display: flex;
    gap: 18px;
    margin-top: auto;
    padding: 0 36px 46px;
  }
  .photo {
    flex: 1;
    height: 140px;
  }
  .photo-workstation { background: linear-gradient(135deg, #3b4a3e 0%, #5a5b52 50%, #2b3137 100%); }
  .photo-network { background: linear-gradient(135deg, #1a2434 0%, #5a3a3a 45%, #c26a2c 70%, #1d2a3a 100%); }

  /* Back */
  .back-body { padding: 40px 40px 0; position: relative; z-index: 1; }
  .back-body .section { margin-bottom: 14px; }
  .back-body .section-title { margin-bottom: 5px; }
  .contact-line {
    color: var(--brand-red);
    font-size: 10px;
    font-style: italic;
    margin-top: 10px;
  }
  .faint-mark {
    position: absolute;
    right: 18px; bottom: 48px;
    width: 200px; height: 200px;
    border: 5px solid var(--faint);
    border-radius: 50%;
  }
</style>
</head>
<body>

  <article class="page page-front">
    <header class="hero">
      <div class="hero-photo" role="img" aria-label="Night sky with stars above a dark silhouette of pine forest"></div>
      <div class="hero-content">
        <div class="brand">
          <span class="brand-dot"></span>
          <span class="brand-name">BRIMVOLT</span>
        </div>
        <h1 class="hero-title">Your Icelandic Partner in Cybersecurity<br>and IT Consultancy</h1>
        <p class="hero-sub">We transform operational challenges into bespoke IT solutions.</p>
      </div>
    </header>

    <div class="front-body">
      <section class="section">
        <h2 class="section-title">Brimvolt ehf your Icelandic IT<br>partner</h2>
        <p class="section-text">Step into a world of comprehensive IT solutions tailored to your unique needs. Our services, available on a contract or as-needed basis, are designed to empower your business and equip you with the tools you need to succeed. More than just a list of offerings, they're a commitment to quality, a dedication to innovation, and a promise of reliability.</p>
      </section>

      <section class="section">
        <h2 class="section-title">Software development and<br>integration services</h2>
        <p class="section-text">We specialize in custom software development across different platforms (server, desktop, embedded systems). We open source software advocates, and decades experience deliver innovative and cost-effective solutions tailored your needs.</p>
        <p class="section-cta">Let's build the perfect software solution for you.</p>
      </section>

      <section class="section">
        <h2 class="section-title">Systems administration</h2>
        <p class="section-text italic">Are you having trouble with your IT infrastructure and in need of qualified personnel care of them? Or do you simply a watchful eye to ensure your systems keep running. We provide on-site and remote sysadmin services to manage your systems and bring you peace of mind.</p>
        <p class="section-cta italic">Take back control.</p>
      </section>
    </div>

    <div class="photo-row">
      <div class="photo photo-workstation" role="img" aria-label="IT professional working at a desk with multiple monitors"></div>
      <div class="photo photo-network" role="img" aria-label="Futuristic server room with glowing network data displays"></div>
    </div>

    <div class="page-band"></div>
  </article>

  <article class="page page-back">
    <div class="back-body">
      <section class="section">
        <h2 class="section-title">Infrastructure monitoring services</h2>
        <p class="section-text">Do you know what is really going on inside your systems? We leverage leading open source monitoring solutions to bring visibility to your infrastructure. Monitor your proactively to ensure that they remain healthy at all times. Collect logs in real time and get notified when problems occur or warnings are raised.</p>
        <p class="section-cta">Fix issues before they become problems.</p>
      </section>

      <section class="section">
        <h2 class="section-title">Automation service</h2>
        <p class="section-text">Because you need effective tools to grow and prosper, it is essential that your align with your operational needs. We offer a comprehensive review of your business and IT environment so as to optimize the means already at your disposal. We streamline workflow and develop new tools as needed, make your IT systems work harder you.</p>
        <p class="section-cta">Let us automate the boring stuff for you.</p>
      </section>

      <section class="section">
        <h2 class="section-title">Technology assessment<br>services</h2>
        <p class="section-text">Unsure about which tools are right for you or what IT strategy to pursue to help your business grow? We conduct market research and perform technical evaluations of software and hardware products to determine the best solutions for your company.</p>
        <p class="section-cta">Let's empower your business with leading-edge solutions.</p>
      </section>

      <section class="section">
        <h2 class="section-title">Security services</h2>
        <p class="section-text">We understand the importance of security in today's digital landscape. That's why we offer comprehensive security services, including network audits to find and remedy flaws that can be exploited to your disadvantage. We perform a thorough review of your IT environment to identify and remediate the issues, to keep your business secure, protect your assets and your reputation. We raise your security posture to the highest standards, so that you don't become the next headline.</p>
        <p class="section-cta">Join us to keep the bad guys out.</p>
      </section>

      <p class="contact-line">Contact us today to discuss your needs.</p>
    </div>

    <div class="faint-mark"></div>
    <div class="page-band"></div>
  </article>

</body>
</html>
```